BEACON CABS

Taxi card design

Need changes very slow in replying to my messages.

Target Market(s)

Customers

Industry/Entity Type

Taxi

Contact Information for Business Card

See previous design

Font styles to use
Sans Serif

Colors
A7469A
B969AE
D3A5CF
EDDBEB
F8F0F9
6B429C
8869AF
B7A5CE
E3DAEB
F3F0F8

Requirements
Nice to have
• We are in the business of looking after people, not just driving vehicles front
Should not have
• Front number 01632 480 480 needs to big big

```html
<!DOCTYPE html>
<html lang="en">
<head>
<meta charset="utf-8">
<title>Beacon Cabs – Business Card</title>
<link rel="stylesheet" href="https://fonts.googleapis.com/css2?family=Exo+2:wght@600;700&family=Montserrat:wght@500&display=swap">
<style>
  :root {
    --plum: #A7469A;
    --plum-light: #B969AE;
    --violet: #6B429C;
    --violet-mid: #8869AF;
    --ink: #161616;
    --card-black: #1c1c1e;
    --paper: #ffffff;
    --steel: #cfcfd2;
    --backdrop: #2a2a2d;
  }
  * { box-sizing: border-box; margin: 0; padding: 0; }
  html, body { width: 1200px; height: 874px; overflow: hidden; }
  body {
    background: var(--backdrop);
    font-family: "Exo 2", sans-serif;
    position: relative;
  }
  .card {
    position: absolute;
    left: 290px;
    width: 620px;
    height: 354px;
    border-radius: 22px;
    overflow: hidden;
  }
  .card-front { top: 63px; background: var(--card-black); }
  .card-back  { top: 457px; background: var(--paper); }

  .brand {
    position: absolute;
    display: flex;
    align-items: center;
    gap: 14px;
    font-weight: 700;
    letter-spacing: 1px;
    white-space: nowrap;
  }
  .brand-mark {
    width: 22px; height: 22px;
    background: var(--plum);
    border-radius: 3px;
  }
  .card-front .brand {
    top: 104px; left: 0; right: 0; justify-content: center;
    font-size: 60px; color: var(--paper);
  }
  .front-phone {
    position: absolute;
    top: 210px; left: 0; right: 0;
    display: flex; justify-content: center; align-items: center; gap: 12px;
    font-size: 40px; font-weight: 600; color: var(--steel);
    white-space: nowrap;
  }
  .icon { display: inline-block; flex: none; }

  .card-back .brand {
    top: 30px; left: 150px;
    font-size: 46px; color: var(--ink);
  }
  .services {
    position: absolute;
    top: 104px; left: 120px; width: 220px;
    text-align: right;
    font-size: 19px; font-weight: 600; line-height: 1.05;
    color: var(--plum);
    text-transform: uppercase;
    white-space: nowrap;
  }
  .back-phone {
    position: absolute;
    top: 170px; left: 20px; width: 320px;
    display: flex; justify-content: flex-end; align-items: center; gap: 8px;
    font-size: 33px; font-weight: 700; color: var(--ink);
    white-space: nowrap;
    line-height: 1;
  }
  .divider {
    position: absolute;
    top: 112px; left: 362px;
    width: 1.5px; height: 118px;
    background: var(--ink);
  }
  .contact {
    position: absolute;
    top: 116px; left: 380px; width: 230px;
    font-family: "Montserrat", sans-serif;
    font-size: 12.5px; font-weight: 500; line-height: 1.35;
    color: #333;
    list-style: none;
  }
  .contact li { display: flex; gap: 8px; align-items: flex-start; margin-bottom: 4px; white-space: nowrap; }
  .contact .icon { margin-top: 2px; }
  .wave { position: absolute; left: 0; top: 0; }
  .band-phones {
    position: absolute;
    left: 0; right: 0; bottom: 20px;
    display: flex; justify-content: space-around;
    padding: 0 20px;
  }
  .band-phone {
    display: flex; align-items: center; gap: 6px;
    font-size: 21px; font-weight: 600; color: var(--paper);
    white-space: nowrap;
  }
</style>
</head>
<body>

  <section class="card card-front" aria-label="Card front">
    <div class="brand"><span class="brand-mark"></span>BEACON CABS</div>
    <div class="front-phone">
      <svg class="icon" width="24" height="30" viewBox="0 0 24 24" aria-hidden="true"><path fill="#A7469A" d="M6.6 10.8a15 15 0 0 0 6.6 6.6l2.2-2.2a1 1 0 0 1 1-.25 11.4 11.4 0 0 0 3.6.57 1 1 0 0 1 1 1V20a1 1 0 0 1-1 1A17 17 0 0 1 3 4a1 1 0 0 1 1-1h3.5a1 1 0 0 1 1 1c0 1.25.2 2.45.57 3.57a1 1 0 0 1-.25 1z"/></svg>
      01632 480 480
    </div>
  </section>

  <section class="card card-back" aria-label="Card back">
    <svg class="wave" width="620" height="354" viewBox="0 0 620 354" aria-hidden="true">
      <defs>
        <linearGradient id="band" x1="0" y1="0" x2="1" y2="0">
          <stop offset="0" stop-color="#A7469A"/>
          <stop offset="1" stop-color="#6B429C"/>
        </linearGradient>
      </defs>
      <path fill="url(#band)" d="M0 238 C120 214 230 304 420 298 C520 295 585 306 620 332 L620 354 L0 354 Z"/>
      <path fill="#B969AE" opacity=".45" d="M440 304 C530 301 590 314 620 342 L620 354 L560 354 C560 334 520 312 440 304 Z"/>
    </svg>

    <div class="brand"><span class="brand-mark"></span>BEACON CABS</div>

    <p class="services">Minibuses<br>Airport Transfers<br>School Transport</p>

    <div class="back-phone">
      <svg class="icon" width="20" height="24" viewBox="0 0 24 24" aria-hidden="true"><path fill="#A7469A" d="M6.6 10.8a15 15 0 0 0 6.6 6.6l2.2-2.2a1 1 0 0 1 1-.25 11.4 11.4 0 0 0 3.6.57 1 1 0 0 1 1 1V20a1 1 0 0 1-1 1A17 17 0 0 1 3 4a1 1 0 0 1 1-1h3.5a1 1 0 0 1 1 1c0 1.25.2 2.45.57 3.57a1 1 0 0 1-.25 1z"/></svg>
      <span>01632 480 480</span>
    </div>

    <div class="divider"></div>

    <ul class="contact">
      <li>
        <svg class="icon" width="11" height="14" viewBox="0 0 24 30" aria-hidden="true"><path fill="#A7469A" d="M12 0a11 11 0 0 0-11 11c0 8 11 19 11 19s11-11 11-19A11 11 0 0 0 12 0zm0 15a4 4 0 1 1 0-8 4 4 0 0 1 0 8z"/></svg>
        <span>Harbour Lane Depot<br>Quay St, Millbrook<br>MB4 7QX</span>
      </li>
      <li>
        <svg class="icon" width="11" height="12" viewBox="0 0 24 24" aria-hidden="true"><path fill="#A7469A" d="M6.6 10.8a15 15 0 0 0 6.6 6.6l2.2-2.2a1 1 0 0 1 1-.25 11.4 11.4 0 0 0 3.6.57 1 1 0 0 1 1 1V20a1 1 0 0 1-1 1A17 17 0 0 1 3 4a1 1 0 0 1 1-1h3.5a1 1 0 0 1 1 1c0 1.25.2 2.45.57 3.57a1 1 0 0 1-.25 1z"/></svg>
        <span>Free Ph: 0800 555 0 199</span>
      </li>
      <li>
        <svg class="icon" width="12" height="10" viewBox="0 0 24 18" aria-hidden="true"><path fill="#A7469A" d="M0 0h24v18H0z"/><path fill="none" stroke="#fff" stroke-width="2" d="M1 1l11 9 11-9"/></svg>
        <span>bookings@beaconcabs.co.uk</span>
      </li>
      <li>
        <svg class="icon" width="11" height="11" viewBox="0 0 24 24" aria-hidden="true"><circle cx="12" cy="12" r="11" fill="#A7469A"/><path fill="none" stroke="#fff" stroke-width="1.6" d="M1 12h22M12 1c4 4 4 18 0 22M12 1c-4 4-4 18 0 22"/></svg>
        <span>www.beaconcabs.co.uk</span>
      </li>
    </ul>

    <div class="band-phones">
      <span class="band-phone"><svg class="icon" width="14" height="16" viewBox="0 0 24 24" aria-hidden="true"><path fill="#fff" d="M6.6 10.8a15 15 0 0 0 6.6 6.6l2.2-2.2a1 1 0 0 1 1-.25 11.4 11.4 0 0 0 3.6.57 1 1 0 0 1 1 1V20a1 1 0 0 1-1 1A17 17 0 0 1 3 4a1 1 0 0 1 1-1h3.5a1 1 0 0 1 1 1c0 1.25.2 2.450.57 3.57a1 1 0 0 1-.25 1z"/></svg>01632 960 101</span>
      <span class="band-phone"><svg class="icon" width="14" height="16" viewBox="0 0 24 24" aria-hidden="true"><path fill="#fff" d="M6.6 10.8a15 15 0 0 0 6.6 6.6l2.2-2.2a1 1 0 0 1 1-.25 11.4 11.4 0 0 0 3.6.57 1 1 0 0 1 1 1V20a1 1 0 0 1-1 1A17 17 0 0 1 3 4a1 1 0 0 1 1-1h3.5a1 1 0 0 1 1 1c0 1.25.2 2.45.57 3.57a1 1 0 0 1-.25 1z"/></svg>01632 960 202</span>
      <span class="band-phone"><svg class="icon" width="14" height="16" viewBox="0 0 24 24" aria-hidden="true"><path fill="#fff" d="M6.6 10.8a15 15 0 0 0 6.6 6.6l2.2-2.2a1 1 0 0 1 1-.25 11.4 11.4 0 0 0 3.6.57 1 1 0 0 1 1 1V20a1 1 0 0 1-1 1A17 17 0 0 1 3 4a1 1 0 0 1 1-1h3.5a1 1 0 0 1 1 1c0 1.25.2 2.45.57 3.57a1 1 0 0 1-.25 1z"/></svg>01632 960 303</span>
    </div>
  </section>

</body>
</html>
```